Pecan Ridge Paving. Chip Seal Done Right

I need my card to have all my basic information on it. Keep it simple. Include web site, phone number and email address. Include phrase Chip Seal Done Right or Pecan Ridge’s Top Paving Company. Keep card simple. Include color and logo. Put all contact info on card. Make card simple and not complicated.

Here is infuriation yo out in business card

Dale R. Whitmore
830.555.0173 cell phone
Dalewhitmore7@mailbarn.net
www.pecanridgepaving.net

Target Market(s)

Hill Country Texas USA

Industry/Entity Type

Road chip seal

Contact Information for Business Card

We chip seal roads for ranches and property owners

Font styles to use
Serif
Sans Serif
Decorative
Script

Colors
0054AA
0677BA
7BADD7
CADEEF
E8F1F8
EB3D1F
EC4F4E
F09395
F8D3D4
FCEDEE

Requirements
Must have
• Keep it simply
Nice to have
• Logo and all basic info

```html
<!DOCTYPE html>
<html lang="en">
<head>
<meta charset="utf-8">
<title>Pecan Ridge Paving — Business Card</title>
<link href="https://fonts.googleapis.com/css2?family=Open+Sans:wght@400;600;800&display=swap" rel="stylesheet">
<style>
  :root {
    --navy: #151b52;
    --navy-deep: #111643;
    --red: #b01e2e;
    --ink: #3a3a44;
    --paper: #ffffff;
    --stage: #e4e5ea;
    --faint-red: #f6dfe1;
    --faint-grey: #ebecf0;
  }
  * { box-sizing: border-box; margin: 0; padding: 0; }
  html, body { width: 1200px; height: 800px; overflow: hidden; }
  body {
    background: var(--stage);
    font-family: "Open Sans", sans-serif;
    display: flex;
    align-items: center;
    justify-content: center;
    gap: 60px;
  }
  .card {
    width: 525px;
    height: 300px;
    position: relative;
    overflow: hidden;
    box-shadow: 0 6px 18px rgba(20, 24, 60, 0.15);
  }

  /* Back */
  .card--back { background: var(--navy); }
  .card--back .pattern {
    position: absolute; inset: 0;
    background: linear-gradient(135deg, var(--navy) 0%, var(--navy-deep) 100%);
  }
  .card--back .brand-mark {
    position: absolute;
    right: 34px; bottom: 34px;
    display: flex; align-items: center; gap: 8px;
    color: var(--paper);
    font-weight: 800;
    font-size: 13px;
    letter-spacing: 0.5px;
  }
  .brand-dot {
    width: 14px; height: 14px; border-radius: 50%;
    background: var(--red);
    flex: none;
  }

  /* Front */
  .card--front { background: var(--paper); }
  .card--front .watermark {
    position: absolute;
    left: 60px; top: 70px;
    width: 160px; height: 230px;
    background: linear-gradient(160deg, var(--faint-red) 0%, var(--faint-grey) 100%);
    border-radius: 80px 40px 0 0;
  }
  .brand {
    position: absolute;
    left: 26px; top: 22px;
    display: flex; align-items: flex-start; gap: 8px;
  }
  .brand .brand-dot { width: 20px; height: 20px; margin-top: 4px; }
  .brand__name {
    color: var(--navy);
    font-weight: 800;
    font-size: 17px;
    line-height: 19px;
    text-transform: uppercase;
    letter-spacing: 0.3px;
  }
  .brand__tagline {
    margin-top: 4px;
    padding-top: 3px;
    border-top: 1px solid var(--red);
    color: var(--red);
    font-size: 8px;
    font-weight: 600;
    letter-spacing: 0.6px;
    text-transform: uppercase;
    text-align: right;
  }
  .holder {
    position: absolute;
    right: 26px; top: 110px;
    text-align: right;
  }
  .holder__name {
    color: var(--red);
    font-weight: 800;
    font-size: 16px;
    text-transform: uppercase;
    letter-spacing: 0.4px;
  }
  .holder__title {
    color: var(--ink);
    font-size: 15px;
  }
  .contacts {
    position: absolute;
    right: 26px; bottom: 30px;
    width: 300px;
    list-style: none;
    border-bottom: 2px solid var(--navy);
    padding-bottom: 6px;
  }
  .contacts li {
    display: flex;
    justify-content: flex-end;
    align-items: center;
    gap: 7px;
    color: var(--ink);
    font-size: 14.5px;
    line-height: 22px;
    white-space: nowrap;
  }
  .contacts svg { width: 13px; height: 13px; fill: var(--red); flex: none; }
</style>
</head>
<body>

  <section class="card card--back" aria-label="Card back">
    <div class="pattern" role="img" aria-label="Repeating tone-on-tone brand pattern in navy"></div>
    <div class="brand-mark"><span class="brand-dot"></span>Pecan Ridge Paving</div>
  </section>

  <section class="card card--front" aria-label="Card front">
    <div class="watermark" role="img" aria-label="Faint large brand symbol as background decoration"></div>

    <div class="brand">
      <span class="brand-dot"></span>
      <div>
        <p class="brand__name">Pecan Ridge<br>Paving</p>
        <p class="brand__tagline">Chip Seal Done Right</p>
      </div>
    </div>

    <div class="holder">
      <p class="holder__name">Dale R. Whitmore</p>
      <p class="holder__title">Director</p>
    </div>

    <ul class="contacts">
      <li>830.555.0173
        <svg viewBox="0 0 24 24" aria-hidden="true"><path d="M6.6 10.8a15.1 15.1 0 0 0 6.6 6.6l2.2-2.2a1 1 0 0 1 1-.25 11.4 11.4 0 0 0 3.6.57 1 1 0 0 1 1 1V20a1 1 0 0 1-1 1A17 17 0 0 1 3 4a1 1 0 0 1 1-1h3.5a1 1 0 0 1 1 1c0 1.250.2 2.45.57 3.57a1 1 0 0 1-.25 1z"/></svg>
      </li>
      <li>Dalewhitmore7@mailbarn.net
        <svg viewBox="0 0 24 24" aria-hidden="true"><path d="M3 5h18a1 1 0 0 1 1 1v12a1 1 0 0 1-1 1H3a1 1 0 0 1-1-1V6a1 1 0 0 1 1-1zm9 7.5L20 7H4z"/></svg>
      </li>
      <li>www.pecanridgepaving.net
        <svg viewBox="0 0 24 24" aria-hidden="true"><path d="M12 2a10 10 0 1 0 0 20 10 10 0 0 0 0-20zm6.9 6h-3a15 15 0 0 0-1.3-3.9A8 8 0 0 1 18.9 8zM12 4c.8 1.2 1.5 2.5 1.9 4h-3.8c.4-1.5 1.1-2.8 1.9-4zM4.3 14a8 8 0 0 1 0-4h3.4a16 16 0 0 0 0 4zm.8 2h3a15 15 0 0 0 1.3 3.9A8 8 0 0 1 5.1 16zm3-8h-3a8 8 0 0 1 4.3-3.9A15 15 0 0 0 8.1 8zM12 20c-.8-1.2-1.5-2.5-1.9-4h3.8c-.4 1.5-1.1 2.8-1.9 4zm2.3-6H9.7a14 14 0 0 1 0-4h4.6a14 14 0 0 1 0 4zm.3 5.9a15 15 0 0 0 1.3-3.9h3a8 8 0 0 1-4.3 3.9zm1.7-5.9a16 16 0 0 0 0-4h3.4a8 8 0 0 1 0 4z"/></svg>
      </li>
      <li>12 dummy city, dummy place 0000
        <svg viewBox="0 0 24 24" aria-hidden="true"><path d="M12 2a7 7 0 0 0-7 7c0 5.2 7 13 7 13s7-7.8 7-13a7 7 0 0 0-7-7zm0 9.5A2.5 2.5 0 1 1 12 6.5a2.5 2.5 0 0 1 0 5z"/></svg>
      </li>
    </ul>
  </section>

</body>
</html>
```